Flyer-Design für verschiedene Anwendungsfälle bzw. Produkte
Zielgruppe
Wir lösen reale Probleme mit digitalen Technologien wie IoT und KI. In unseren Projekten liefern wir Gesamtlösungen von der Strategieberatung über Konzepterstellung bis zur technischen Umsetzung und dem Betrieb. Integration und Konzeption spielen eine große Rolle, wir sind kein Hardwareanbieter, sondern bauen Komplettlösungen aus Software, Connectivity und Hardware. Unsere Kunden sind gehobener Mittelstand bis Konzern, ab 25 Mio € aufwärts. Oft sind unsere Kunden aus konservativen Branchen. Wir müssen beim Design immer einen Kompromiss aus innovativ und Vertrauen erweckend finden. Unsere Persona ist weiß, männlich, über 50, nicht besonders technologieaffin.
Aufgabenstellung
Wir brauchen eine Flyer-Vorlage für verschiedene Anwendungsfälle bzw. Produkte. Im Anhang sind Beispiele für Produktbeschreibungen, sowie ein Flyer, den wir selbst designet haben.
Ergebnis soll ein Flyer-Design sein, das wir für solche Produkte immer wieder verwenden können, DIN A5 zweiseitig.
Exo2 und Trebuchet sind unsere Schriftarten. Logos habe ich in 2 Formaten angehängt.
Website: tavolu.me
Wenn Sie weitere Ideen haben, sind wir ganz Ohr.
Grafisch bitte nur die Farben grau, schwarz und orange verwenden (grau und orange siehe Logo)

```html
<!DOCTYPE html>
<html lang="de">
<head>
<meta charset="utf-8">
<title>Flyer – Füllstandsüberwachung</title>
<link rel="stylesheet" href="https://fonts.googleapis.com/css2?family=Montserrat:wght@400;500;600;700;800&display=swap">
<style>
  :root{
    --canvas:#e4e4e4;
    --paper:#f7f7f6;
    --ink:#1e1e1e;
    --navy:#1d2738;
    --orange:#e8801f;
    --white:#ffffff;
  }
  *{box-sizing:border-box;margin:0;padding:0}
  html,body{width:1200px;height:900px;overflow:hidden;background:var(--canvas);font-family:"Montserrat",sans-serif;color:var(--ink)}
  .stage{position:relative;width:1200px;height:900px}
  .page{position:absolute;top:68px;width:540px;height:764px;background:var(--paper);overflow:hidden;box-shadow:0 8px 24px rgba(0,0,0,.15)}
  .page--front{left:45px}
  .page--back{left:615px}

  /* Front */
  .hero{position:absolute;left:0;top:0;width:540px;height:296px}
  .hero__photo{position:absolute;inset:0}
  .hero__title{position:absolute;left:34px;top:40px;color:var(--white);font-weight:800;font-size:42px;line-height:1.05}
  .hero__subtitle{position:absolute;left:60px;top:188px;color:var(--white);font-weight:700;font-size:18px;line-height:1.3}
  .brand{position:absolute;right:34px;top:180px;display:flex;align-items:center;gap:8px}
  .brand__name{font-weight:500;font-size:28px;letter-spacing:6px;color:var(--orange)}
  .brand__dot{width:9px;height:9px;border-radius:50%;background:var(--orange)}

  .cases{position:absolute;left:28px;top:312px;width:484px;display:flex;gap:20px}
  .case{flex:1;min-width:0}
  .case__label{font-weight:700;font-size:17px;color:var(--orange);margin-bottom:4px}
  .case__lead{font-weight:500;font-size:13.5px;line-height:1.3;color:var(--orange);margin-bottom:8px}
  .case__list{list-style:none;font-size:13px;line-height:1.3;font-weight:500}
  .case__list li{margin-bottom:3px}

  .contact{position:absolute;left:0;bottom:0;width:540px;height:118px}
  .contact__shapes{position:absolute;inset:0}
  .contact__item{position:absolute;display:flex;align-items:center;gap:7px;color:var(--white);font-size:12.5px;font-weight:500;line-height:1.25}
  .contact__item svg{flex:none}
  .contact__item--address{left:20px;top:36px}
  .contact__item--phone{left:20px;top:90px}
  .contact__item--mobile{left:196px;top:90px}
  .contact__item--mail{left:356px;top:90px}

  /* Back */
  .band{position:absolute;left:0;width:540px;background:var(--navy)}
  .band--top{top:0;height:22px}
  .band--bottom{bottom:0;height:52px;display:flex;align-items:center;justify-content:center;color:var(--white);font-weight:700;font-size:15px;letter-spacing:.5px}
  .back__content{position:absolute;left:36px;top:48px;width:468px;text-align:center}
  .tag{display:inline-block;background:var(--orange);color:var(--white);font-weight:700;font-size:14px;padding:3px 14px;margin-bottom:10px}
  .copy{font-size:12.5px;line-height:1.42;font-weight:500}
  .copy p{margin-bottom:4px}
  .hardware{position:relative;margin:22px 0 20px;border:2px solid var(--orange);padding:24px 18px 18px}
  .hardware .tag{position:absolute;left:50%;top:-14px;transform:translateX(-50%);margin:0}
  .hardware__media{margin-top:14px;height:88px}
  .frontend .tag{margin-bottom:10px}
</style>
</head>
<body>
<div class="stage">

  <section class="page page--front">
    <header class="hero">
      <svg class="hero__photo" width="540" height="296" viewBox="0 0 540 296" role="img" aria-label="Nachtaufnahme der Erde aus dem All mit Stadtlichtern">
        <defs>
          <radialGradient id="earth" cx="60%" cy="85%" r="80%">
            <stop offset="0" stop-color="#6a6a6a"/>
            <stop offset=".45" stop-color="#3a3a3a"/>
            <stop offset="1" stop-color="#151515"/>
          </radialGradient>
        </defs>
        <polygon points="0,0 540,0 540,110 400,110 340,296 0,296" fill="url(#earth)"/>
      </svg>
      <h1 class="hero__title">LoRaWAN<br>oder<br>NB-IoT:</h1>
      <p class="hero__subtitle">Füllstandsüberwachung<br>und Routenoptimierung<br>Abfallwirtschaft</p>
      <div class="brand"><span class="brand__dot"></span><span class="brand__name">TAVOLU</span></div>
    </header>

    <div class="cases">
      <article class="case">
        <h2 class="case__label">Fall 1:</h2>
        <p class="case__lead">große öffentliche Container, z.B. Altglas, Altkleider, Altpapier Nutzen und Vorteile</p>
        <ul class="case__list">
          <li>- Bürger wissen, zu welchen Containern sie ihren Abfall bringen können</li>
          <li>- Entsorger kann optimiert leeren und Kosten sparen</li>
          <li>- Containerstandorte können datengestützt erweitert oder reduziert werden</li>
          <li>- Weniger wilder Müll</li>
        </ul>
      </article>
      <article class="case">
        <h2 class="case__label">Fall 2:</h2>
        <p class="case__lead">Kleinere städtische Mülleimer, z.B. in Erholungsgebieten Nutzen und Vorteile</p>
        <ul class="case__list">
          <li>- Nutzung der Mülleimer ist stark von unregelmäßigen Faktoren wie Wetter oder Veranstaltungen abhängig</li>
          <li>- Starr regelmäßige Leerung führt häufig zu Überfüllung und dadurch Umweltverschmutzung, die durch die Anwendung von Sensoren vermieden wird</li>
          <li>- Überflüssige Leerungen werden vermieden und dadurch Kosten gespart</li>
        </ul>
      </article>
    </div>

    <footer class="contact">
      <svg class="contact__shapes" width="540" height="118" viewBox="0 0 540 118">
        <polygon points="0,24 300,24 244,80 0,80" fill="var(--orange)"/>
        <polygon points="0,80 244,80 300,24 540,24 540,118 0,118" fill="var(--navy)"/>
      </svg>
      <div class="contact__item contact__item--address">
        <svg width="16" height="16" viewBox="0 0 16 16"><circle cx="8" cy="8" r="8" fill="#fff"/><path d="M4 8.5 8 4.5l4 4v3.5H9.5V9.5h-3V12H4z" fill="var(--orange)"/></svg>
        <span>Lindenallee 8, 40210,<br>Düsseldorf</span>
      </div>
      <div class="contact__item contact__item--phone">
        <svg width="16" height="16" viewBox="0 0 16 16"><circle cx="8" cy="8" r="8" fill="#fff"/><path d="M5 4.5c.5-.5 1.2-.3 1.4.2l.6 1.4c.2.4 0 .8-.3 1l-.6.4c.5 1 1.3 1.8 2.3 2.3l.4-.6c.2-.3.6-.5 1-.3l1.4.6c.5.2.7.9.2 1.4-1 1-2.6.8-4.3-.9S4 5.5 5 4.5z" fill="var(--navy)"/></svg>
        <span>0211 5550142</span>
      </div>
      <div class="contact__item contact__item--mobile">
        <svg width="16" height="16" viewBox="0 0 16 16"><circle cx="8" cy="8" r="8" fill="#fff"/><rect x="5.5" y="3.5" width="5" height="9" rx="1" fill="var(--navy)"/><rect x="6.3" y="4.5" width="3.4" height="6" fill="#fff"/></svg>
        <span>+49 170 5550187</span>
      </div>
      <div class="contact__item contact__item--mail">
        <svg width="16" height="16" viewBox="0 0 16 16"><circle cx="8" cy="8" r="8" fill="#fff"/><rect x="4" y="5" width="8" height="6" fill="var(--navy)"/><path d="M4 5l4 3.5L12 5" stroke="#fff" fill="none"/></svg>
        <span>consulting@tavolu.me</span>
      </div>
    </footer>
  </section>

  <section class="page page--back">
    <div class="band band--top"></div>
    <div class="back__content">
      <div class="functions">
        <span class="tag">Funktionsweise</span>
        <div class="copy">
          <p>-Im Container werden Sensoren zur Füllstandsmessung angebracht.</p>
          <p>- Der Füllstand wird an eine Bürger-Website/ -App gemeldet, die nur „voll“, „fast voll“ und „nicht voll“ anzeigt, sowie bei voll oder fast voll eine möglichst nahe gelegene Alternative.</p>
          <p>- Der Füllstand wird an den Entsorger gemeldet. Hier kann entweder eine Routenoptimierungs-App zur Verfügung gestellt oder die Daten in ein bestehendes Betriebsführungssystem integriert werden.</p>
          <p>- Die Daten werden analysiert, um die regelmäßige Auslastung der Container zu bestimmen und ihre Standorte langfristig zu optimieren.</p>
        </div>
      </div>

      <div class="hardware">
        <span class="tag">Hardware</span>
        <p class="copy">Ultraschall-, Radar- oder optische Sensoren messen den Abstand zwischen sich selbst und der Oberfläche und erkennen so den Füllstand</p>
        <svg class="hardware__media" width="428" height="88" viewBox="0 0 428 88" role="img" aria-label="Produktfotos verschiedener Füllstandssensoren">
          <defs>
            <linearGradient id="sensor" x1="0" y1="0" x2="0" y2="1">
              <stop offset="0" stop-color="#4a4a4a"/><stop offset="1" stop-color="#1a1a1a"/>
            </linearGradient>
          </defs>
          <rect x="0" y="0" width="428" height="88" fill="url(#sensor)" opacity=".85"/>
        </svg>
      </div>

      <div class="frontend">
        <span class="tag">Frontend und Benachrichtigungen</span>
        <div class="copy">
          <p>-Darstellung in einer Web App (für Mobilgeräte und PCs) auf einer Karte für Bürger, mit Anzeige von Alternativen bei vollen Containern</p>
          <p>- Einbindung in Routenoptimierungs- oder Betriebsführungs-Anwendung beim Entsorger</p>
          <p>- Alarmierung bei Überschreitung von Grenzwerten möglich</p>
        </div>
      </div>
    </div>
    <div class="band band--bottom">www.tavolu.me</div>
  </section>

</div>
</body>
</html>
```